AWESOME RETAILER OF PHONE ACCESSORIES NEEDS AWESOME WEBSITE FROM AWESOME DESIGNER

We currently do not have any website and are looking for one for our new store. We are a retailer who sells bramblefone accessories, speakers, electronics, cables with the best pricing guaranteed. We carry all top name brands including:

TuffNest : http://www.tuffnest.example/en/

Quillcase : http://www.quillcase.example/

Zendra : http://www.zendra.example/Default.asp

Varolux : http://www.varolux.example/

Keen Kit : http://www.keen-kit.example/

http://www.glintshield.example/hot-sellers/bramble-fone-5-crystl-white.html

http://www.fal-toromfg.example/products/detail.cfm?prodID=2

http://marlowqt.example/

http://www.plix.example/

We would like to see our logo's used and a website that is trendy and catchy to our demographics. Our demographic is male/female between the ages of 16-45.

Target Market(s)

Male/Femal Ages -16-45

Industry/Entity Type

Electronics

Requirements
Must have
• Must use our logo's and be a catchy fun website keeps the customers eye.
Coupon Tab where customers can print coupons
Products Tab where we can display all of our brands of products
Contact us page
Location Page
CHATTERWALL/PEEPCAST ACCOUNT TO BE LINKED TO SITE
WEBSITE WILL BE HOSTED BY HOSTRIVET.EXAMPLE PLEASE MAKE SURE YOUR DESIGN IS COMPATIBLE WITH THEM.

PLEASE BE SURE TO USE OUR LOGO IN YOUR DESIGN YOU SUBMIT, THEY ARE ATTACHED TO THIS PROJECT
Nice to have
• We would like a slot where a video can be posted from clipvault
Authorized dealer banner
Should not have
• not a dark website but bright and vibrant
Do not use any logos or images that are trademarked by Bramble.

```html
<!DOCTYPE html>
<html lang="en">
<head>
<meta charset="utf-8">
<title>Tellvo — Phone Accessories</title>
<link href="https://fonts.googleapis.com/css2?family=Oswald:wght@400;500&family=Questrial&family=Open+Sans+Condensed:wght@300;700&family=Arimo:wght@400;700&display=swap" rel="stylesheet">
<style>
:root{
  --backdrop:#2e2a29;
  --page:#ffffff;
  --lime:#9fcb3a;
  --lime-bright:#99cc00;
  --logo-green:#7fbf1f;
  --ink:#222222;
  --text:#555555;
  --dark-panel:#3f3f3f;
  --nav-active:#2a2a2a;
  --rule:#dddddd;
  --link:#2a7ab8;
  --grey-btn:#9a9a9a;
}
*{margin:0;padding:0;box-sizing:border-box}
html,body{width:1200px;height:1000px;overflow:hidden;background:var(--backdrop);font-family:"Arimo",Arial,sans-serif}
.page{position:absolute;left:174px;top:70px;width:854px;height:910px;background:var(--page)}
.abs{position:absolute}

.brand{left:164px;top:28px;display:flex;align-items:center;gap:8px}
.brand-mark{width:14px;height:14px;background:var(--logo-green)}
.brand-name{font-family:"Oswald",sans-serif;font-weight:400;font-size:30px;color:var(--logo-green);line-height:1}

.nav-band{left:1px;top:95px;width:843px;height:26px;background:linear-gradient(#a9d343,#92c12c)}
.nav{left:120px;top:95px;height:26px;display:flex;list-style:none}
.nav li{font-family:"Oswald",sans-serif;font-size:11px;color:#fff;line-height:26px;padding:0 9px;border-right:1px solid #5f7f1c;text-shadow:0 1px 0 rgba(0,0,0,.35)}
.nav li:first-child{border-left:1px solid #5f7f1c}
.nav li.active{background:var(--nav-active);color:#ddd}
.search{left:581px;top:99px;display:flex;gap:3px}
.search-field{width:94px;height:19px;border-radius:10px;background:#fff;font-size:10px;color:#444;padding:3px 9px}
.search-btn{width:45px;height:19px;background:var(--grey-btn);color:#fff;font-family:"Oswald",sans-serif;font-size:9px;text-align:center;line-height:19px}

.slider{left:120px;top:125px;width:603px;height:255px;overflow:hidden;background:#fff}
.slide-title{left:31px;top:12px;font-family:"Questrial",sans-serif;font-size:54px;color:var(--logo-green);line-height:1}
.slide-desc{left:28px;top:97px;width:212px;font-family:"Questrial",sans-serif;font-size:12.5px;line-height:16.5px;color:#9a9a9a}
.slide-photo{left:306px;top:20px;width:280px;height:235px;background:radial-gradient(ellipse at 50% 40%,#f4f4f4,#dcdcdc 60%,#fff 90%)}
.arrow{width:25px;height:25px;border-radius:50%;background:#8d8d8d;color:#fff;font-size:14px;text-align:center;line-height:24px;font-weight:700}
.caption{left:0;top:202px;width:603px;height:53px;background:rgba(55,55,55,.95);color:#fff;padding:8px 10px}
.caption h2{font-family:"Oswald",sans-serif;font-weight:400;font-size:14px;margin-bottom:5px}
.caption p{font-size:8.5px}

.module-head{height:22px;background:var(--lime);color:#fff;font-family:"Oswald",sans-serif;font-size:11px;line-height:22px;padding-left:7px;letter-spacing:.3px}
.latest{left:120px;top:400px;width:139px;height:177px;border:1px solid var(--rule)}
.latest-photo{left:3px;top:28px;width:131px;height:92px;background:radial-gradient(ellipse at 50% 55%,#4a4a4a,#1e1e1e 45%,#c8c8c8 70%,#fff 90%)}
.latest-caption{left:3px;top:119px;width:131px;height:40px;background:var(--dark-panel);color:#fff;font-family:"Oswald",sans-serif;font-size:13px;padding:7px 9px}
.small-arrow{width:26px;height:26px;border-radius:50%;border:2px solid rgba(255,255,255,.8);background:rgba(120,120,120,.5);color:#fff;font-size:12px;text-align:center;line-height:22px}

.video{left:275px;top:400px;width:307px;height:222px;background:#000}
.share{left:266px;width:32px;height:32px;background:#111;display:flex;align-items:center;justify-content:center}
.share-blank{width:12px;height:12px;background:#ddd}
.play{left:137px;top:87px;width:32px;height:32px;background:#151515;display:flex;align-items:center;justify-content:center}
.controls{left:0;top:206px;width:307px;height:16px;background:#1a1a1a;color:#ddd;font-size:8px;line-height:16px}
.track{left:52px;top:4px;width:183px;height:8px;background:#000}

.login{left:584px;top:400px;width:138px;height:212px;border:1px solid var(--rule)}
.login label{position:absolute;left:3px;font-size:8px;color:#333}
.field{position:absolute;left:4px;width:110px;height:19px;border:1px solid #ccc;font-size:8px;color:#999;line-height:17px;padding-left:21px}
.field::before{content:"";position:absolute;left:0;top:0;width:16px;height:17px;background:#eee;border-right:1px solid #ccc}
.remember{left:4px;top:112px;font-size:8px;color:#333;display:flex;align-items:center;gap:4px}
.box{width:8px;height:8px;border:1px solid #999;background:#fff}
.login-btn{left:4px;top:126px;width:39px;height:19px;background:#a8a8a8;color:#fff;font-family:"Oswald",sans-serif;font-size:8px;text-align:center;line-height:19px}
.login-links{left:14px;top:153px;list-style:none}
.login-links li{font-size:8px;color:var(--link);line-height:15px;display:flex;align-items:center;gap:6px}
.login-links li::before{content:"";width:6px;height:6px;background:#999}

.repair{left:584px;top:618px;width:138px;height:134px;border:1px solid var(--rule);overflow:hidden}
.repair-photo{left:3px;top:2px;width:130px;height:132px;background:linear-gradient(#ffffff,#d8d8d8)}
.repair-title{left:0;top:6px;width:136px;text-align:center;font-family:"Open Sans Condensed",sans-serif;font-weight:700;font-size:15px;color:#222}
.repair-device{left:41px;top:32px;width:54px;height:100px;border-radius:7px;background:linear-gradient(135deg,#2c2c2c,#5a5a5a 50%,#1b1b1b)}

.article{left:275px;top:640px;width:292px;font-size:8.5px;line-height:15px;color:var(--text)}

.tagline{left:0;top:797px;width:854px;text-align:center;font-family:"Open Sans Condensed",sans-serif;font-weight:300;font-size:29px;color:var(--ink);letter-spacing:.2px}
.tagline span{color:var(--logo-green)}

.footer{left:60px;top:845px;width:707px;height:65px;background:var(--lime-bright);border-top:2px solid #555}
.social{left:66px;top:14px;display:flex;gap:5px}
.social i{display:block;width:21px;height:21px;background:#fff;opacity:.85;border-radius:2px}
.copyright{left:64px;top:52px;font-size:7px;color:#fff}
.credit{left:522px;top:52px;font-size:6px;color:#3a5a00}
</style>
</head>
<body>
<div class="page">
  <div class="abs brand"><span class="brand-mark"></span><span class="brand-name">Tellvo</span></div>

  <div class="abs nav-band"></div>
  <ul class="abs nav">
    <li class="active">HOME</li><li>PRODUCTS</li><li>ABOUT US</li><li>SIGN UP</li><li>CONTACT US</li><li>REPAIR</li>
  </ul>
  <div class="abs search"><div class="search-field">Search...</div><div class="search-btn">SEARCH</div></div>

  <div class="abs slider">
    <div class="abs slide-photo" role="img" aria-label="White phone charging cable connectors photo"></div>
    <div class="abs slide-title">cables</div>
    <p class="abs slide-desc">Description about cables which sell by tellvo.Description about cables which sell by tellvo.Description about cables which sell by tellvo.</p>
    <div class="abs arrow" style="left:12px;top:89px">&#10094;</div>
    <div class="abs arrow" style="left:566px;top:89px">&#10095;</div>
    <div class="abs caption">
      <h2>Cables</h2>
      <p>Pellentesque habitant morbi tristique senectus et netus et malesuada fames ac turpis egestas. In posuere felis nec tortor. Pellentesque faucibus.</p>
    </div>
  </div>

  <div class="abs latest">
    <div class="module-head">LATEST PRODUCTS</div>
    <div class="abs latest-photo" role="img" aria-label="Portable round speaker product photo"></div>
    <div class="abs small-arrow" style="left:13px;top:70px">&#10094;</div>
    <div class="abs small-arrow" style="left:96px;top:70px">&#10095;</div>
    <div class="abs latest-caption">Product 4</div>
  </div>

  <div class="abs video">
    <div class="abs share" style="top:9px"><span class="share-blank"></span></div>
    <div class="abs share" style="top:49px"><span class="share-blank"></span></div>
    <div class="abs share" style="top:88px"><svg width="16" height="12" viewBox="0 0 16 12"><path d="M5 1 L1 6 L5 11 M11 1 L15 6 L11 11" stroke="#fff" stroke-width="2" fill="none"/></svg></div>
    <div class="abs play"><svg width="12" height="14" viewBox="0 0 12 14"><path d="M1 1 L11 7 L1 13Z" fill="#fff"/></svg></div>
    <div class="abs controls">
      <svg class="abs" style="left:6px;top:4px" width="8" height="9" viewBox="0 0 8 9"><path d="M0 0 L8 4.5 L0 9Z" fill="#ddd"/></svg>
      <span class="abs" style="left:23px">00:00</span>
      <div class="abs track"></div>
      <span class="abs" style="left:245px">00:00</span>
      <svg class="abs" style="left:274px;top:4px" width="10" height="9" viewBox="0 0 10 9"><path d="M0 3 H3 L6 0 V9 L3 6 H0Z" fill="#ddd"/></svg>
      <svg class="abs" style="left:292px;top:4px" width="9" height="9" viewBox="0 0 9 9"><path d="M0 3 V0 H3 M6 0 H9 V3 M9 6 V9 H6 M3 9 H0 V6" stroke="#ddd" fill="none"/></svg>
    </div>
  </div>

  <div class="abs login">
    <div class="module-head">LOGIN</div>
    <label style="top:30px">User Name</label>
    <div class="field" style="top:44px">User Name</div>
    <label style="top:71px">Password</label>
    <div class="field" style="top:85px">Password</div>
    <div class="abs remember"><span class="box"></span>Remember Me</div>
    <div class="abs login-btn">LOG IN</div>
    <ul class="abs login-links">
      <li>Forgot your password?</li><li>Forgot your username?</li><li>Create an account</li>
    </ul>
  </div>

  <div class="abs repair">
    <div class="abs repair-photo" role="img" aria-label="Phone with cracked screen being repaired"></div>
    <div class="abs repair-device"></div>
    <div class="abs repair-title">We fix bramblefones</div>
  </div>

  <p class="abs article">Phasellus felis dolor, scelerisque a, tempus eget, lobortis id, libero. Donec scelerisque leo ac risus. Praesent sit amet est. In dictum, dolor eu dictum porttitor, enim felis viverra mi, eget luctus massa purus quis odio. Etiam nulla massa, pharetra facilisis, volutpat in, imperdiet sit amet, sem. Aliquam nec erat at purus cursus interdum. Vestibulum ligula augue, bibendum accumsan, luctus eu, malesuada ut, tincidunt sed, diam. Donec quis mi sed magna hendrerit accumsan. Suspendisse risus nibh, ultricies eu, volutpat non, condimentum hendrerit, augue. Etiam eleifend, metus vitae adipiscing semper, mauris ipsum iaculis elit, congue gravida elit mi egestas orci. Curabitur pede.</p>

  <div class="abs tagline">SEE HOW PEOPLE LIVE IN <span>DIFFERENT</span> LIFE STYLE</div>

  <footer class="abs footer">
    <div class="abs social"><i></i><i></i><i></i><i></i></div>
    <div class="abs copyright">Copyright By Tellvo 2013</div>
    <div class="abs credit">Tallowly 3.0 Templates by Brightrow Hosting</div>
  </footer>
</div>
</body>
</html>
```